Strategy and Technology Consulting - Our Story and Values Page

Interior Page design – Our History and Our Values

Our homepage has been designed and we are looking for a design for one of the interior pages. This interior page tells the story of Our History and Our Values

Because the homepage has been designed, we would like this interior page to reflect the design of the homepage without being a mirror image of the homepage.

This site will be implemented in WordPress using the Elementor framework.

Font: Poppins medium and Poppins dark
Illustrations: Our homepage illustrations were designed by “Welmo 1974” on Pixaborne. Compatible original or stock illustrations are welcome. Stock photography is also welcome. Welmo is also available through Welmo Trastek on Folivane

Uploaded Files
• Homepage design – this is the design we will use for our homepage. Contest entries should reflect this basic style but should be distinctly different from the homepage.
• Our History and Our Values – Wireframe – the basic layout of the page we are looking for.
• Our History and Our Values – Word document with the text supporting the wireframe.
• Color Palette – please use colors compatible with the palette attached.

Our Story - timeline
There is a timeline element in the wireframe. The wireframe displays this as a series of chevrons (arrows), but it does not need to be. Creativity in display of the timeline is appreciated.

Our Values
If you look at the Word document, you will see that there are a lot of words on the page. The winning design will present the information in a way that engages the user without overwhelming them with too much to read. For example, they may click on a value and see more information.

Target Market(s)

CIO's and Technology Executives

Number of Pages Required

1 page

Font styles to use
Sans Serif
Other font styles liked:
• Poppin

Requirements
Must have
• A timeline element, all of our values
Nice to have
• Clever timeline display

```html
<!DOCTYPE html>
<html lang="en">
<head>
<meta charset="utf-8">
<title>Quorvex – Our Story and Values</title>
<link href="https://fonts.googleapis.com/css2?family=Poppins:wght@400;500;600;700;800&display=swap" rel="stylesheet">
<style>
:root{
  --navy:#23588c;
  --blue:#2b6699;
  --blue-soft:#6b97be;
  --ink:#34465f;
  --text:#7a7f88;
  --yellow:#f0b323;
  --slate:#4a5670;
  --slate-dark:#3a4358;
  --white:#ffffff;
  --line:#e9eef4;
}
*{box-sizing:border-box;margin:0;padding:0}
html,body{width:1200px;height:4205px;overflow:hidden}
body{font-family:'Poppins',sans-serif;background:var(--white);position:relative;color:var(--ink)}

/* header */
.site-header{position:absolute;left:0;top:0;width:1200px;height:95px;background:var(--white)}
.brand{position:absolute;left:92px;top:22px;font-size:42px;font-weight:400;color:#8d96a3;letter-spacing:1px;line-height:50px;display:flex;align-items:center;gap:10px}
.brand-dot{width:12px;height:12px;border-radius:50%;background:var(--blue)}
.main-nav{position:absolute;left:544px;top:36px;display:flex;align-items:center;gap:22px;font-size:12.5px;font-weight:600;color:var(--ink)}
.main-nav span::after{content:" ⌄";font-size:11px}
.btn-yellow{position:absolute;background:var(--yellow);color:var(--white);font-weight:700;border-radius:30px;display:flex;align-items:center;justify-content:center;letter-spacing:.4px}
.header-cta{left:980px;top:28px;width:130px;height:37px;font-size:12px}

/* story */
.story{position:absolute;left:0;top:95px;width:1200px;height:800px;background:linear-gradient(200deg,#225b8f 0%,#2b6699 45%,#5f8db6 85%,#86a9c8 100%)}
.section-title{position:absolute;left:0;width:1200px;text-align:center;font-weight:800;font-size:44px;letter-spacing:.5px}
.story-title{top:148px;color:var(--white)}
.story-wave{position:absolute;left:0;top:690px}
.era-card{position:absolute;top:265px;width:328px;height:393px;background:var(--white)}
.era-tag{position:absolute;top:-31px;left:46px;height:66px;width:236px}
.era-tag svg{position:absolute;left:0;top:0}
.era-label{position:absolute;left:14px;top:0;width:200px;height:66px;display:flex;align-items:center;justify-content:center;color:var(--white);font-weight:700;font-size:31px;gap:8px;white-space:nowrap}
.era-label small{font-size:14px;line-height:15px;font-weight:700;text-align:center}
.era-item{position:absolute;left:28px;display:flex;gap:12px;align-items:flex-start;font-size:16.5px;font-weight:500;color:#2f4663;line-height:24px}
.era-item svg{flex:none;margin-top:-2px}
.era-sub{position:absolute;left:78px;font-size:15.5px;color:var(--text);line-height:26px}

/* values */
.values-title{top:852px;color:var(--ink)}
.value-card{position:absolute;left:90px;width:1020px;height:326px;background:var(--white);box-shadow:0 6px 28px rgba(40,60,90,.09)}
.value-art{position:absolute;left:32px;top:40px;width:254px;height:246px;border-radius:50%;background:radial-gradient(ellipse at 50% 55%,#d5e3f3 0%,#e9f0f9 55%,rgba(255,255,255,0) 72%)}
.value-body{position:absolute;left:318px;top:0;width:660px;height:326px;display:flex;flex-direction:column;justify-content:center}
.value-name{font-size:34px;font-weight:700;color:var(--ink);line-height:40px;margin-bottom:22px}
.value-copy{font-size:15.5px;line-height:25px;color:var(--text)}

/* newsletter + footer */
.footer-band{position:absolute;left:0;top:3500px;width:1200px;height:647px}
.newsletter{position:absolute;left:139px;top:3495px;width:922px;height:207px;border-radius:104px;background:var(--yellow)}
.newsletter h2{position:absolute;left:78px;top:62px;font-size:31px;font-weight:800;color:var(--white)}
.newsletter p{position:absolute;left:79px;top:112px;width:420px;font-size:14.5px;line-height:18px;font-weight:500;color:var(--white)}
.email-field{position:absolute;left:547px;top:81px;width:320px;height:46px;border-radius:23px;background:var(--white);display:flex;align-items:center;padding-left:22px;gap:10px;font-size:12px;color:#8e95a0}
.email-send{position:absolute;right:6px;top:6px;width:34px;height:34px;border-radius:50%;background:#9aa3ae}
.footer-brand{position:absolute;left:120px;top:3880px;font-size:62px;font-weight:400;color:var(--white);letter-spacing:1px;display:flex;align-items:center;gap:12px}
.footer-brand .brand-dot{background:var(--yellow);width:14px;height:14px}
.social{position:absolute;top:3959px;width:42px;height:42px;border-radius:50%;background:rgba(255,255,255,.22)}
.footer-cta{left:214px;top:4025px;width:131px;height:36px;font-size:12px}
.foot-col{position:absolute;top:3858px;color:var(--white)}
.foot-col h3{font-size:19px;font-weight:700;margin-bottom:14px}
.foot-col li{list-style:none;font-size:12px;line-height:31px}
.foot-col li::before{content:"› ";}
.contact-row{display:flex;gap:10px;font-size:12px;line-height:17px;margin-bottom:18px}
.contact-row svg{flex:none;margin-top:2px}
.copyright{position:absolute;left:0;top:4147px;width:1200px;height:58px;background:var(--slate-dark);color:var(--white);font-size:13px;display:flex;align-items:center;justify-content:center}
.chat{position:absolute;left:1134px;top:4107px;width:48px;height:48px;border-radius:50%;background:var(--yellow);display:flex;align-items:center;justify-content:center}
</style>
</head>
<body>

<header class="site-header">
  <div class="brand"><span class="brand-dot"></span>Quorvex</div>
  <nav class="main-nav">
    <svg width="14" height="13" viewBox="0 0 14 13"><path d="M1 6.5 7 1l6 5.5V12H8.5V8.5h-3V12H1z" fill="#8d96a3"/></svg>
    <span>ABOUT US</span><span>SERVICES</span><span>INSIGHTS</span><span>JOIN US</span>
  </nav>
  <div class="btn-yellow header-cta">CONTACT US</div>
</header>

<section class="story"></section>
<svg class="story-wave" width="1200" height="210" viewBox="0 0 1200 210">
  <path d="M0 88 C150 140 300 20 520 28 C720 36 950 150 1200 205 L1200 210 L0 210Z" fill="#dce9f5"/>
  <path d="M0 80 C150 130 300 40 520 38 C720 40 950 140 1200 210 L0 210Z" fill="#ffffff"/>
</svg>
<h1 class="section-title story-title">OUR STORY</h1>

<div class="era-card" style="left:90px">
  <div class="era-tag"><svg width="236" height="66"><path d="M10 2H204L230 33L204 64H10L28 33Z" fill="none" stroke="#fff" stroke-width="3"/><path d="M20 8H198L220 33L198 58H20L36 33Z" fill="#23588c"/></svg><div class="era-label">2017–2019</div></div>
  <div class="era-item" style="top:80px"><svg width="30" height="28" fill="none" stroke="#34465f" stroke-width="1.6"><path d="M2 26h26M5 26V14h5v12M12 26V6h5v20M19 26V11h5v15"/></svg>Growth Strategy Focus</div>
  <div class="era-item" style="top:142px"><svg width="30" height="28" fill="none" stroke="#34465f" stroke-width="1.6"><circle cx="14" cy="14" r="11"/><path d="M14 3v11h11"/></svg>Consistent, Modest Growth</div>
  <div class="era-item" style="top:204px"><svg width="30" height="28" fill="none" stroke="#34465f" stroke-width="1.6"><rect x="2" y="3" width="26" height="16"/><path d="M10 25h10M15 19v6M6 8h18M6 13h12"/></svg>Preliminary Focus on<br>Technology</div>
  <div class="era-item" style="top:292px"><svg width="30" height="30" fill="none" stroke="#34465f" stroke-width="1.6"><path d="M15 3a9 9 0 0 0-5 16v4h10v-4a9 9 0 0 0-5-16zM11 27h8"/></svg><span><b>Eureka!</b> &nbsp;Implementing<br>strategy is hard.</span></div>
</div>

<div class="era-card" style="left:436px">
  <div class="era-tag"><svg width="236" height="66"><path d="M10 2H204L230 33L204 64H10L28 33Z" fill="none" stroke="#fff" stroke-width="3"/><path d="M20 8H198L220 33L198 58H20L36 33Z" fill="#23588c"/></svg><div class="era-label">2020–2021</div></div>
  <div class="era-item" style="top:80px"><svg width="30" height="30" fill="none" stroke="#34465f" stroke-width="1.6"><rect x="11" y="2" width="8" height="7"/><rect x="2" y="21" width="8" height="7"/><rect x="20" y="21" width="8" height="7"/><path d="M15 9v6M6 21v-6h18v6"/></svg>Pandemic Pauses Growth</div>
  <div class="era-item" style="top:138px"><svg width="30" height="30" fill="none" stroke="#34465f" stroke-width="1.6"><rect x="2" y="2" width="12" height="10"/><rect x="16" y="18" width="12" height="10"/><path d="M8 12v11h8M22 18V7h-8"/></svg>Rethinking :</div>
  <div class="era-sub" style="top:173px">- the business model<br>- the delivery model</div>
</div>

<div class="era-card" style="left:782px">
  <div class="era-tag"><svg width="236" height="66"><path d="M10 2H204L230 33L204 64H10L28 33Z" fill="none" stroke="#fff" stroke-width="3"/><path d="M20 8H198L220 33L198 58H20L36 33Z" fill="#23588c"/></svg><div class="era-label">2022 <small>AND<br>ONWARD</small></div></div>
  <div class="era-item" style="top:80px"><svg width="30" height="30" fill="none" stroke="#34465f" stroke-width="1.6"><circle cx="15" cy="6" r="4"/><path d="M8 17h14M15 10v7M6 17v5M24 17v5"/><circle cx="6" cy="25" r="3"/><circle cx="24" cy="25" r="3"/></svg>Leadership Team for Focus<br>on Essential Areas</div>
  <div class="era-item" style="top:162px"><svg width="30" height="30" fill="none" stroke="#34465f" stroke-width="1.6"><circle cx="15" cy="15" r="12"/><path d="M11 18l3 3 6-9"/></svg>Rapid Growth</div>
  <div class="era-item" style="top:224px"><svg width="30" height="30" fill="none" stroke="#34465f" stroke-width="1.6"><circle cx="15" cy="15" r="12"/><path d="M15 7l2.4 5 5.4.6-4 3.6 1.1 5.3L15 18.8l-4.9 2.7 1.1-5.3-4-3.6 5.4-.6z"/></svg>Customer Success</div>
</div>

<h2 class="section-title values-title">OUR VALUES</h2>

<article class="value-card" style="top:936px">
  <div class="value-art" role="img" aria-label="Isometric illustration of a team building a growth platform"></div>
  <div class="value-body"><h3 class="value-name">The Value of Every Human.<br>Regardless.</h3><p class="value-copy">Each person's unique experiences and perspectives add vibrant hues to the tapestry of our shared existence. &nbsp;In a world where diversity paints the canvas of humanity, true beauty is found in recognizing the inherent and incalculable value of every human being.</p></div>
</article>
<article class="value-card" style="top:1290px">
  <div class="value-art" role="img" aria-label="Isometric illustration of colleagues working together around a shared desk"></div>
  <div class="value-body"><h3 class="value-name">Collaboration</h3><p class="value-copy">Collaboration in work transforms individual endeavors into symphonies of collective achievement. Through collaboration, diverse talents converge, fostering a rich exchange of ideas that amplifies creativity, accelerates progress, and brings forth solutions beyond what a single mind could conceive.</p></div>
</article>
<article class="value-card" style="top:1646px">
  <div class="value-art" role="img" aria-label="Isometric illustration of a route from point A to point B on a platform"></div>
  <div class="value-body"><h3 class="value-name">Passion</h3><p class="value-copy">Passion infuses our work with energy, transforming routine tasks into opportunities for creativity and innovation. Fueled by passion, individuals become unstoppable forces, driven to overcome challenges and achieve remarkable outcomes that benefit them and inspire those around them.</p></div>
</article>
<article class="value-card" style="top:2000px">
  <div class="value-art" role="img" aria-label="Illustration of a developer at a desk surrounded by ideas"></div>
  <div class="value-body"><h3 class="value-name">Excellence</h3><p class="value-copy">Excellence isn't a destination; it's a continuous journey of refinement and growth. Striving for excellence cultivates a culture of continuous improvement, fostering innovation, credibility, and a lasting impact that resonates far beyond the immediate task.</p></div>
</article>
<article class="value-card" style="top:2356px">
  <div class="value-art" role="img" aria-label="Isometric illustration of a city with buildings and a drone"></div>
  <div class="value-body"><h3 class="value-name">Tenacity</h3><p class="value-copy">Tenacity is the unwavering anchor that keeps us grounded amidst adversity, propelling us forward when faced with obstacles. The resilience to persist, adapt, and learn from setbacks leads to the mastery of skills and the fulfillment of ambitious goals.</p></div>
</article>
<article class="value-card" style="top:2712px">
  <div class="value-art" role="img" aria-label="Illustration of people around large interface screens"></div>
  <div class="value-body"><h3 class="value-name">Solution Mindset</h3><p class="value-copy">A solution mindset is the compass that directs our focus from problems to possibilities. It empowers us to navigate challenges with a proactive mindset, igniting a journey of exploration and innovation that not only resolves issues but also paves the way for continuous growth and success.</p></div>
</article>
<article class="value-card" style="top:3068px">
  <div class="value-art" role="img" aria-label="Illustration of a team with gears and progress charts"></div>
  <div class="value-body"><h3 class="value-name">Generosity</h3><p class="value-copy">Generosity creates a virtuous cycle of goodwill, fostering a sense of unity and shared purpose among colleagues. By freely sharing knowledge, support, and resources, we uplift those around us and contribute to a collaborative environment where collective achievements flourish.</p></div>
</article>

<svg class="footer-band" width="1200" height="647" viewBox="0 0 1200 647">
  <defs><linearGradient id="slateFill" x1="0" y1="0" x2="1" y2="1"><stop offset="0" stop-color="#3f4b63"/><stop offset="1" stop-color="#55617a"/></linearGradient></defs>
  <path d="M0 40 C80 20 140 70 200 140 L1000 140 C1080 40 1150 20 1200 30 L1200 647 L0 647Z" fill="url(#slateFill)"/>
  <path d="M200 215 C330 250 420 330 600 300 C780 270 880 230 1000 215 Z" fill="#ffffff"/>
  <path d="M230 228 C360 275 430 345 600 318 C780 290 880 245 990 222" fill="none" stroke="#d7dbe2" stroke-width="6"/>
</svg>

<div class="newsletter">
  <h2>Subscribe Our Newsletter</h2>
  <p>Subscribe our newsletter to receive the latest news and exclusive offers every week, No spam.</p>
  <div class="email-field">
    <svg width="13" height="10"><rect x=".5" y=".5" width="12" height="9" fill="#8e95a0"/><path d="M1 1l5.5 4.5L12 1" stroke="#fff" fill="none"/></svg>
    Enter email address
    <div class="email-send"><svg width="34" height="34"><path d="M11 17l13-6-5 13-2-5z" fill="#fff"/></svg></div>
  </div>
</div>

<div class="footer-brand"><span class="brand-dot"></span>Quorvex</div>
<div class="social" style="left:175px"></div>
<div class="social" style="left:227px"></div>
<div class="social" style="left:278px"></div>
<div class="social" style="left:327px"></div>
<div class="btn-yellow footer-cta">CONTACT US</div>

<div class="foot-col" style="left:490px">
  <h3>Quick links</h3>
  <ul><li>Home</li><li>About Us</li><li>Services</li><li>Insights</li><li>Join Us</li><li>Contact Us</li></ul>
</div>
<div class="foot-col" style="left:668px">
  <h3>Our Services</h3>
  <ul><li>Business Transformation</li><li>ERP Implementations</li><li>ERP Solutions</li><li>BI and Data</li><li>Building the Right Team...</li></ul>
</div>
<div class="foot-col" style="left:898px">
  <h3>Contact info</h3>
  <div class="contact-row"><svg width="12" height="10"><rect width="12" height="10" fill="#f0b323"/><path d="M0 0l6 5 6-5" stroke="#3f4b63" fill="none"/></svg><span>Email:<br>hello@quorvex-mail.com</span></div>
  <div class="contact-row"><svg width="12" height="12"><path d="M2 1l3 0 1 3-2 1.5a7 7 0 0 0 3 3L8.5 6.5l3 1V11c-6 0-10.5-4.5-10.5-10z" fill="#f0b323"/></svg><span>Phone:<br>+44 120 555 0192</span></div>
  <div class="contact-row"><svg width="12" height="14"><path d="M6 13C2 8 1 6.5 1 5a5 5 0 0 1 10 0c0 1.5-1 3-5 8z" fill="#f0b323"/><circle cx="6" cy="5" r="1.8" fill="#3f4b63"/></svg><span>Location:<br>Some address line goes<br>here city name</span></div>
</div>

<div class="copyright">© Quorvex Design 2023, All Rights Reserved</div>
<div class="chat"><svg width="26" height="22"><path d="M3 2h20v13H10l-5 5v-5H3z" fill="#fff"/><circle cx="9" cy="8.5" r="1.5" fill="#f0b323"/><circle cx="13" cy="8.5" r="1.5" fill="#f0b323"/><circle cx="17" cy="8.5" r="1.5" fill="#f0b323"/></svg></div>

</body>
</html>
```